Single Side Postcard Size Flyer Design

We want to design an attractive and eye-catching sign for hair stylists and barbers to sit on their workstations to attract the attention of their clients regarding hair loss and encourage them to speak to their stylist about it of they are would like to seek treatment.
Many men and women suffer from hair loss, but are often in denial it is happening or too embarrassed to talk about it.
This postcard sized flyer is designed to stick to the mirror at their hair stylist or barber and encourage them to ask their stylist about it.
We want this to be very plain and simple. With just perhaps some kind of simple head line and worry lines. I have uploaded a simple idea.
I have also uploaded the print templates that must be used to provide final designs.

Target Market(s)

Men aged 25 to 60 with thinning hair

Industry/Entity Type

Healthcare

Font styles to use
Sans Serif

Colors
0355a3
ffffff
cfcfcf
1b1b1b

Requirements
Must have
• Flyer size is vertical 4" x 6"
• Copy for the flyer is as follows ans is in color blue: #014ca5
• Worried About Thinning Hair?
• 2 out of 3 Men will have visible hair loss by age 35.
• The Good News is that your
• Barber or Stylist can tell you how to
• stop the loss & grow back your hair.
• Just ask.
• The Halt and Renew Program from
• The Velmora Scalp Company
• Fresh Research. No Scalpel. Your Locks.
• www.velmorascalpinfo.example
Should not have
• - dont add any logos, images or ornate design. this needs to be simple, easy to ready and eye catching.
• - do not use the color red in any capacity.

```html
<!DOCTYPE html>
<html lang="en">
<head>
<meta charset="utf-8">
<title>Velmora Scalp Company – Mirror Card</title>
<link rel="stylesheet" href="https://fonts.googleapis.com/css2?family=Roboto+Condensed:wght@500;600;700&display=swap">
<style>
  :root {
    --brand-blue: #2055a0;
    --paper: #ffffff;
    --band-text: #ffffff;
  }
  * { margin: 0; padding: 0; box-sizing: border-box; }
  html, body {
    width: 894px; height: 1200px; overflow: hidden;
    background: var(--paper);
  }
  .flyer {
    position: relative; width: 894px; height: 1200px;
    background: var(--paper);
    font-family: "Roboto Condensed", "Arial Narrow", sans-serif;
    color: var(--brand-blue);
    text-transform: uppercase;
    text-align: center;
  }
  .headline-frame {
    position: absolute; left: 0; top: 0; width: 894px; height: 500px;
  }
  .site-url {
    position: absolute; left: 0; right: 0; top: 88px;
    font-size: 30px; font-weight: 600; letter-spacing: -0.5px; line-height: 34px;
  }
  .headline {
    position: absolute; left: 0; right: 0; top: 178px;
    font-weight: 700; letter-spacing: -1.5px;
  }
  .headline-lead { display: block; font-size: 84px; line-height: 84px; }
  .headline-main { display: block; font-size: 110px; line-height: 104px; letter-spacing: -2px; }
  .statistic {
    position: absolute; left: 0; right: 0; top: 425px;
    font-weight: 600; letter-spacing: -1px;
  }
  .statistic-line1 { display: block; font-size: 30px; line-height: 46px; }
  .statistic-line1 .figure { font-size: 48px; font-weight: 700; }
  .statistic-line2 { display: block; font-size: 29px; line-height: 32px; }
  .message-box {
    position: absolute; left: 73px; top: 551px; width: 752px; height: 568px;
    border: 2px solid var(--brand-blue);
  }
  .message {
    position: absolute; left: 0; right: 0; top: 46px;
    font-size: 56px; font-weight: 700; line-height: 56px; letter-spacing: -2.5px;
  }
  .sign-off {
    position: absolute; left: 0; right: 0; top: 346px;
    font-size: 30px; font-weight: 600; letter-spacing: -1px;
  }
  .company-band {
    position: absolute; left: -2px; right: -2px; bottom: -2px; height: 158px;
    background: var(--brand-blue); color: var(--band-text);
    padding-top: 28px;
  }
  .company-name { font-size: 50px; font-weight: 700; line-height: 52px; letter-spacing: -2px; }
  .company-tagline { font-size: 27px; font-weight: 600; line-height: 34px; letter-spacing: -1px; }
</style>
</head>
<body>
<main class="flyer">
  <svg class="headline-frame" width="894" height="500" viewBox="0 0 894 500" aria-hidden="true">
    <g fill="none" stroke="var(--brand-blue)" stroke-width="2">
      <polyline points="230,105 72,105 72,465 230,465"/>
      <polyline points="664,105 822,105 822,465 664,465"/>
    </g>
  </svg>
  <p class="site-url">www.velmorascalpinfo.example</p>
  <h1 class="headline">
    <span class="headline-lead">Worried About</span>
    <span class="headline-main">Thinning Hair?</span>
  </h1>
  <p class="statistic">
    <span class="statistic-line1"><span class="figure">2</span> out of <span class="figure">3</span> men will have</span>
    <span class="statistic-line2">visible hair loss by age 35</span>
  </p>
  <section class="message-box">
    <p class="message">The good news is that<br>your barber or stylist<br>can tell you how to<br>stop the loss &amp; grow<br>back your hair.</p>
    <p class="sign-off">- Just ask.</p>
    <footer class="company-band">
      <p class="company-name">The Velmora Scalp Company</p>
      <p class="company-tagline">Fresh Research. No Scalpel. Your Locks.</p>
    </footer>
  </section>
</main>
</body>
</html>
```